Wordpress template re-design of current website

We need a WordPress template design and new look for our existing website. Our existing site it located at www.velmoro.com.au We are a tech company and want a fresh, clean modern website that matches our brand, services and logo colors. Our main Services are hospitality solutions, Velmoro TV solution and managed networks, more information on these can come from our existing website.

Target Market(s)

We are a tech company so must have a modern feel for new technology

Industry/Entity Type

It Company

Number of Pages Required

5+ page

Font styles to use
Sans Serif

Requirements
Must have
• Be based on a wordpress templete design and match the services that we have in our existing website, in the testimonials want a place for video testimonials as well as text. Nice clean icons used for graphics to represent services.
Nice to have
• nice visual representation of our services in the way of clean icons etc
Should not have
• Clutter

```html
<!DOCTYPE html>
<html lang="en">
<head>
<meta charset="utf-8">
<title>Velmoro Wireless Internet</title>
<link href="https://fonts.googleapis.com/css2?family=Open+Sans:wght@300;400;600;700&family=Oswald:wght@500;600&display=swap" rel="stylesheet">
<style>
:root{
  --blue:#1565b8;
  --blue-dark:#0d4d94;
  --blue-light:#2a82d9;
  --ink:#333d47;
  --muted:#6c7680;
  --white:#ffffff;
  --dark:#2a2f35;
  --line:#e3e7eb;
}
*{margin:0;padding:0;box-sizing:border-box}
html,body{width:1200px;height:2600px;overflow:hidden}
body{font-family:"Open Sans",Arial,sans-serif;color:var(--ink);background:var(--white);position:relative}

/* header */
.site-header{position:absolute;top:0;left:0;width:1200px;height:140px;background:var(--white);display:flex;align-items:center;justify-content:space-between;padding:0 80px}
.brand{display:flex;align-items:center;gap:14px}
.brand-dot{width:22px;height:22px;border-radius:50%;background:var(--blue)}
.brand-name{font-size:46px;font-weight:700;color:var(--blue)}
.main-nav{display:flex;align-items:center;gap:38px;font-size:18px;color:var(--muted)}
.main-nav .active{color:var(--blue)}
.portal-btn{background:var(--blue);color:var(--white);padding:12px 40px;font-weight:600}

/* hero */
.hero{position:absolute;top:140px;left:0;width:1200px;height:450px;background:linear-gradient(100deg,#f6a53a 0%,#e78a2c 25%,#b9a28a 55%,#8fa8bf 80%,#6f90ad 100%)}
.hero-copy{position:absolute;left:300px;top:56px;color:var(--white)}
.hero-title{font-family:"Oswald",Arial,sans-serif;font-weight:600;font-size:50px;line-height:58px;letter-spacing:1px;text-transform:uppercase}
.hero-sub{font-size:20px;margin-top:4px}
.hero-phone{display:flex;align-items:center;gap:16px;margin-top:30px;font-size:40px;font-weight:700}
.hero-phone .icon{width:52px;height:52px;border-radius:50%;background:var(--blue);display:flex;align-items:center;justify-content:center}
.slider-dots{position:absolute;left:560px;bottom:26px;display:flex;gap:10px}
.slider-dots span{width:14px;height:14px;border-radius:50%;background:rgba(255,255,255,.55)}
.slider-dots span.on{background:var(--blue)}

/* welcome */
.welcome{position:absolute;top:590px;left:0;width:1200px;height:310px;background:var(--blue);color:var(--white);text-align:center;padding-top:70px}
.welcome h1{font-weight:400;font-size:44px}
.welcome h2{font-weight:600;font-size:26px;margin-top:4px}
.welcome p{font-size:16px;width:720px;margin:36px auto 0;line-height:26px}

/* services */
.services{position:absolute;top:900px;left:0;width:1200px;height:790px}
.services-lead{position:absolute;left:0;top:70px;width:1200px;text-align:center;font-size:35px;font-weight:400;line-height:50px;color:var(--ink)}
.services-lead span{display:block;white-space:nowrap}
.service-list{position:absolute;left:72px;top:220px;width:720px}
.service{display:flex;gap:34px;margin-bottom:28px;align-items:flex-start}
.service:nth-child(2){margin-left:40px}
.service:nth-child(3){margin-left:100px}
.service:nth-child(4){margin-left:200px;margin-bottom:0}
.service-icon{flex:none;width:96px;height:96px;border-radius:50%;background:var(--blue-dark);border:5px solid #d9e6f3;display:flex;align-items:center;justify-content:center}
.service h3{font-size:23px;font-weight:400;color:var(--blue);margin-top:6px}
.service p{font-size:14px;color:var(--muted);line-height:21px;margin-top:6px;width:320px}
.services-photo{position:absolute;left:770px;top:230px;width:400px;height:470px;border-radius:6px;background:radial-gradient(ellipse at 55% 50%,#e6ebf0 0%,#ffffff 72%)}

/* testimonials */
.testimonials{position:absolute;top:1690px;left:0;width:1200px;height:450px;background:linear-gradient(180deg,#3a4047,#22272c);color:var(--white)}
.testimonials h2{text-align:center;font-size:44px;font-weight:400;margin-top:36px}
.video-box{position:absolute;left:72px;top:160px;width:316px;height:212px;background:linear-gradient(135deg,#2f3e4c,#1a242d);border:3px solid #4a5560;display:flex;align-items:center;justify-content:center}
.play{width:62px;height:62px;border-radius:50%;background:rgba(255,255,255,.18);display:flex;align-items:center;justify-content:center}
.quote{position:absolute;left:420px;top:160px;width:700px;font-size:16px;line-height:24px;color:#dfe3e7}
.quote cite{display:block;font-style:normal;margin-top:20px;font-size:16px;color:var(--white)}
.arrow{position:absolute;top:240px}
.arrow.left{left:28px}
.arrow.right{right:28px}

/* clients */
.clients{position:absolute;top:2140px;left:0;width:1200px;height:260px;text-align:center}
.clients h2{font-size:44px;font-weight:400;margin-top:42px;color:var(--ink)}
.clients h2 span{color:var(--blue)}
.client-row{display:flex;justify-content:space-between;align-items:center;padding:0 80px;margin-top:60px}
.client{font-size:24px;font-weight:700;color:#4a525a}

/* footer */
.site-footer{position:absolute;top:2400px;left:0;width:1200px;height:200px;background:var(--blue);color:var(--white)}
.footer-links{position:absolute;left:80px;top:36px;display:flex;gap:40px;font-size:18px}
.footer-social{position:absolute;right:80px;top:22px;display:flex;gap:22px}
.footer-social span{width:56px;height:56px;border-radius:50%;background:var(--white);color:var(--blue);font-size:13px;font-weight:600;display:flex;align-items:center;justify-content:center}
.footer-rule{position:absolute;left:80px;right:80px;top:98px;height:1px;background:rgba(255,255,255,.35)}
.footer-contact{position:absolute;left:80px;top:118px;width:1040px;display:flex;justify-content:space-between;align-items:center;font-size:14px;line-height:20px}
.contact-item{display:flex;align-items:center;gap:16px}
.contact-item .ring{width:52px;height:52px;border-radius:50%;border:2px solid var(--white);display:flex;align-items:center;justify-content:center}
.contact-item.phone{font-size:20px;font-weight:600}
</style>
</head>
<body>

<header class="site-header">
  <div class="brand"><span class="brand-dot"></span><span class="brand-name">Velmoro</span></div>
  <nav class="main-nav">
    <span class="active">HOME</span><span>ABOUT</span><span>SERVICES</span><span>OUR WORK</span><span>CONTACT</span>
    <span class="portal-btn">PORTAL</span>
  </nav>
</header>

<section class="hero" role="img" aria-label="Photo of hikers raising their arms on a mountain ridge at sunset">
  <div class="hero-copy">
    <div class="hero-title">Networks designed for<br>high-speed performance</div>
    <div class="hero-sub">Help your business achieve high speed connectivity!</div>
    <div class="hero-phone">
      <span class="icon"><svg width="26" height="26" viewBox="0 0 24 24"><path fill="#fff" d="M6.6 10.8a15.1 15.1 0 0 0 6.6 6.6l2.2-2.2c.3-.3.7-.4 1-.2 1.1.4 2.3.6 3.6.6.6 0 1 .4 1 1V20c0 .6-.4 1-1 1A17 17 0 0 1 3 4c0-.6.4-1 1-1h3.5c.6 0 1 .4 1 1 0 1.3.2 2.5.6 3.6.1.3 0 .7-.2 1z"/></svg></span>
      1300 415 962
    </div>
  </div>
  <div class="slider-dots"><span class="on"></span><span></span><span></span></div>
</section>

<section class="welcome">
  <h1>Welcome to Velmoro Wireless Internet</h1>
  <h2>Creating solutions that work.</h2>
  <p>Velmoro Wireless has been a leader in wireless networks and internet billing systems for over a decade. Velmoro currently has completed over 1000 installations.</p>
</section>

<section class="services">
  <p class="services-lead"><span>We strive to out work our competition with an effective approach</span><span>and a powerful skill set, which is why were industry leading.</span></p>
  <div class="service-list">
    <div class="service">
      <div class="service-icon"><svg width="46" height="46" viewBox="0 0 24 24" fill="none" stroke="#fff" stroke-width="2" stroke-linecap="round"><path d="M2 9a15 15 0 0 1 20 0"/><path d="M5.5 12.5a10 10 0 0 1 13 0"/><path d="M9 16a5 5 0 0 1 6 0"/><circle cx="12" cy="19.5" r="1" fill="#fff"/></svg></div>
      <div><h3>Wi-Fi Hotspots</h3><p>Leading supplier of public access and internet billing systems</p></div>
    </div>
    <div class="service">
      <div class="service-icon"><svg width="44" height="44" viewBox="0 0 24 24" fill="none" stroke="#fff" stroke-width="2" stroke-linecap="round"><rect x="3" y="4" width="18" height="12" rx="1"/><path d="M8 20h8M12 16v4"/></svg></div>
      <div><h3>Velmoro TV</h3><p>Turn your standard TV into a full guest information system and point of sale</p></div>
    </div>
    <div class="service">
      <div class="service-icon"><svg width="44" height="44" viewBox="0 0 24 24" fill="none" stroke="#fff" stroke-width="2" stroke-linecap="round" stroke-linejoin="round"><circle cx="8" cy="12" r="4"/><path d="M12 12h9M18 12v3M15 12v2"/></svg></div>
      <div><h3>HSIA Solutions</h3><p>Our guest access solutions have been built with the guest in mind and are easy to use</p></div>
    </div>
    <div class="service">
      <div class="service-icon"><svg width="44" height="44" viewBox="0 0 24 24" fill="none" stroke="#fff" stroke-width="2" stroke-linejoin="round"><path d="M4 5h16v10H10l-5 4v-4H4z"/></svg></div>
      <div><h3>Social Wi-Fi</h3><p>Get more out of your existing Wi-Fi with our social plug-ins to gain valuable insight into users</p></div>
    </div>
  </div>
  <div class="services-photo" role="img" aria-label="Photo of a young man sitting cross-legged using a tablet"></div>
</section>

<section class="testimonials">
  <h2>What Our Client Say</h2>
  <svg class="arrow left" width="22" height="44" viewBox="0 0 22 44"><path d="M18 4 4 22l14 18" fill="none" stroke="#fff" stroke-width="3"/></svg>
  <div class="video-box" role="img" aria-label="Video testimonial still of a client speaking">
    <span class="play"><svg width="24" height="24" viewBox="0 0 24 24"><path d="M8 5v14l11-7z" fill="#fff"/></svg></span>
  </div>
  <blockquote class="quote">
    “Installing Velmoro Internet Solution has been a great experience for this business. The staff were very professional and easy to work with and good at lateral options to consider that would work best for the business. The installation was easy and happened without any problems at all. The system is easy to use for both guests and staff, which can be tailored to suit the needs of the guest and business, which was a deciding factor. I would highly recommend Velmoro to anyone in room internet solution”
    <cite>Mark Delaney – Harbor Suites</cite>
  </blockquote>
  <svg class="arrow right" width="22" height="44" viewBox="0 0 22 44"><path d="M4 4l14 18L4 40" fill="none" stroke="#fff" stroke-width="3"/></svg>
</section>

<section class="clients">
  <h2>Our <span>Clients</span></h2>
  <div class="client-row">
    <span class="client">Lodgeway</span>
    <span class="client">Tripora</span>
    <span class="client">Campora</span>
    <span class="client">Stayvale</span>
    <span class="client">Coachline</span>
    <span class="client">Ridgemont</span>
  </div>
</section>

<footer class="site-footer">
  <nav class="footer-links"><span>Case Studies</span><span>Testimonials</span><span>News</span><span>Resellers</span></nav>
  <div class="footer-social"><span>Share</span><span>Post</span></div>
  <div class="footer-rule"></div>
  <div class="footer-contact">
    <div class="contact-item">
      <span class="ring"><svg width="22" height="22" viewBox="0 0 24 24"><path fill="#fff" d="M12 2a7 7 0 0 0-7 7c0 5 7 13 7 13s7-8 7-13a7 7 0 0 0-7-7zm0 9.5A2.5 2.5 0 1 1 12 6.5a2.5 2.5 0 0 1 0 5z"/></svg></span>
      <span>42 Harbour Lane<br>Coral Bay, QLD 4300</span>
    </div>
    <div class="contact-item phone">
      <span class="ring"><svg width="22" height="22" viewBox="0 0 24 24"><path fill="#fff" d="M6.6 10.8a15.1 15.1 0 0 0 6.6 6.6l2.2-2.2c.3-.3.7-.4 1-.2 1.1.4 2.3.6 3.6.6.6 0 1 .4 1 1V20c0 .6-.4 1-1 1A17 17 0 0 1 3 4c0-.6.4-1 1-1h3.5c.6 0 1 .4 1 1 0 1.3.2 2.5.6 3.6.1.3 0 .7-.2 1z"/></svg></span>
      <span>1300 415 962</span>
    </div>
    <div class="contact-item">
      <span class="ring"><svg width="22" height="22" viewBox="0 0 24 24" fill="none" stroke="#fff" stroke-width="2"><rect x="3" y="5" width="18" height="14" rx="1"/><path d="m3 6 9 7 9-7"/></svg></span>
      <span>sales@velmoro.com.au</span>
    </div>
    <div class="contact-item">
      <span>© 2015 Velmoro Wireless.<br>All Rights Reserved.</span>
    </div>
  </div>
</footer>

</body>
</html>
```